Qarawan Silk Business Card and Stationary
QS Business Card & Stationary
Qarawan Silk Business Card and Stationary - Trade
Creative Brief
Professional
Khalid Omar Al Fayez خالد عمر الفايز
Chief Executive Officer مدير التنفيذي
Qarawan Silk Rimal Plaza Business Center Sawari Street , Jeddah 21587 Kingdom of Saudi Arabia
+966 12 6847315 Ext. 354
khalidomar.fayez@qarawansilk.com
www.qarawansilk.com
Name and Title is required to be in English & Arabic, Give it a try with Logo Fonts - Not a must. BC & Stationary must look like modern and decent design.
Large Company Logo QR Code Web Address Nimbo apps market and Tapu Shop Logos
qarawan qarawan
Dear designers, Only business card designs are being posted, What about stationary designs?
Revised logo is already uploaded on the contest.
pixelcraft587 pixelcraft587
do you have a logo?

```html
<!DOCTYPE html>
<html lang="en">
<head>
<meta charset="utf-8">
<title>Qarawan Silk – Business Card and Stationery</title>
<link href="https://fonts.googleapis.com/css2?family=Montserrat:wght@400;500;600;700&family=Cairo:wght@400;600&display=swap" rel="stylesheet">
<style>
  :root{
    --maroon:#7b1521;
    --maroon-dark:#65101a;
    --gold:#d2a94f;
    --ink:#2b2b2b;
    --muted:#6d6d6d;
    --paper:#ffffff;
    --night:#0e0e0e;
    --stage:#ececec;
  }
  *{margin:0;padding:0;box-sizing:border-box}
  html,body{width:1200px;height:881px;overflow:hidden}
  body{background:var(--stage);font-family:"Montserrat",Arial,sans-serif;color:var(--ink);position:relative}
  .piece{position:absolute;overflow:hidden}
  .ar{font-family:"Cairo",Arial,sans-serif}
  .brand{display:flex;align-items:center;gap:6px;font-weight:700;letter-spacing:.08em;text-transform:uppercase;white-space:nowrap}
  .brand .dot{border-radius:50%;flex:none}
  .brand.gold{color:var(--gold)} .brand.gold .dot{background:var(--gold)}
  .brand.red{color:var(--maroon)} .brand.red .dot{background:var(--maroon)}
  .small{font-size:5.5px;line-height:1.55}

  /* business cards */
  .card{width:230px;height:120px}
  .card-black{left:106px;top:12px;background:var(--night)}
  .card-black .brand{position:absolute;left:14px;top:52px;font-size:8px;letter-spacing:.05em;gap:5px}
  .card-black .brand .dot{width:14px;height:14px}
  .card-black .details{position:absolute;left:124px;top:22px;width:100px;color:#e6e6e6;font-size:5px;line-height:1.6;white-space:nowrap}
  .card-black .details .name{color:var(--gold);font-weight:600;font-size:6.5px;line-height:1.3}
  .card-black .details .name-ar{color:var(--gold);font-size:6px;line-height:1.4}
  .card-black .details .role{color:#bdbdbd}
  .card-black .details .block{margin-top:4px}
  .card-red{background:var(--maroon)}
  .card-red.top{left:355px;top:12px}
  .card-red.bottom{left:355px;top:149px}
  .card-red .brand{position:absolute;left:0;right:0;top:44px;justify-content:center;font-size:12px}
  .card-red .brand .dot{width:20px;height:20px}
  .card-red .badges{position:absolute;left:70px;bottom:10px;display:flex;gap:5px}
  .card-red .badges span{width:18px;height:12px;background:#c9a46a;border-radius:1px}
  .card-white{left:106px;top:149px;background:var(--paper)}
  .card-white .brand{position:absolute;left:0;right:0;top:10px;justify-content:center;font-size:8px}
  .card-white .brand .dot{width:12px;height:12px}
  .card-white .name{position:absolute;left:0;right:0;top:34px;text-align:center;color:var(--maroon);font-weight:700;font-size:9px;white-space:nowrap}
  .card-white .name .ar{font-weight:600;font-size:8px;margin-left:4px}
  .card-white .title{position:absolute;left:0;right:0;top:47px;text-align:center;font-size:5px;color:var(--muted);white-space:nowrap}
  .card-white .contacts{position:absolute;left:12px;top:66px}
  .card-white .contacts li{list-style:none;display:flex;align-items:center;gap:3px}
  .card-white .contacts i{width:4px;height:4px;background:var(--maroon);border-radius:50%;display:block}
  .card-white .address{position:absolute;right:12px;top:66px;text-align:right}
  .card-white .address b{color:var(--maroon)}

  /* envelopes */
  .envelope{width:480px;height:216px;background:var(--paper)}
  .envelope-front{left:106px;top:307px}
  .envelope-front .band{height:42px;background:var(--maroon);border-bottom:3px solid var(--gold);padding:12px 0 0 14px}
  .envelope-front .brand{font-size:9px}
  .envelope-front .brand .dot{width:14px;height:14px}
  .envelope-front .sender{position:absolute;left:14px;top:56px;font-size:6px;line-height:1.6}
  .envelope-front .sender b{color:var(--maroon)}
  .envelope-back{left:106px;top:562px;height:230px}
  .envelope-back svg{position:absolute;left:0;top:0}
  .envelope-back .brand{position:absolute;left:0;right:0;top:10px;justify-content:center;font-size:9px}
  .envelope-back .brand .dot{width:14px;height:14px}

  /* letterhead */
  .letterhead{left:605px;top:79px;width:494px;height:737px;background:var(--paper);box-shadow:0 0 0 1px #dcdcdc}
  .letterhead .band{height:60px;background:var(--maroon);border-bottom:3px solid var(--gold);position:relative}
  .letterhead .band .brand{position:absolute;left:14px;top:20px;font-size:10px}
  .letterhead .band .brand .dot{width:18px;height:18px}
  .letterhead .band .col{position:absolute;top:9px;color:#f2e6e6;font-size:5.5px;line-height:1.6;white-space:nowrap}
  .letterhead .band .col b{color:var(--gold)}
  .letterhead .band .col.address{left:192px}
  .letterhead .band .col.contact{left:318px}
  .letterhead .signature{position:absolute;left:16px;top:612px;width:90px;height:16px;background:linear-gradient(90deg,#cfcfcf,#e8e8e8)}
  .letterhead .signee{position:absolute;left:16px;top:633px}
  .letterhead .signee .name{color:var(--maroon);font-weight:700;font-size:10px}
  .letterhead .signee .role{font-size:5.5px;color:var(--muted)}
</style>
</head>
<body>

<!-- business card, black front -->
<section class="piece card card-black">
  <div class="brand gold"><span class="dot"></span>Qarawan Silk</div>
  <div class="details">
    <div class="name">Khalid Omar Al Fayez</div>
    <div class="name-ar ar">خالد عمر الفايز</div>
    <div class="role">Chief Executive Officer</div>
    <div class="block">Rimal Plaza Business Center</div>
    <div>Sawari Street, Jeddah 21587</div>
    <div>+966 12 6847315 Ext. 354</div>
    <div>khalidomar.fayez@qarawansilk.com</div>
    <div>www.qarawansilk.com</div>
  </div>
</section>

<!-- business card, maroon back -->
<section class="piece card card-red top">
  <div class="brand gold"><span class="dot"></span>Qarawan Silk</div>
  <div class="badges"><span></span><span role="img" aria-label="QR code"></span><span></span></div>
</section>

<!-- business card, white front -->
<section class="piece card card-white">
  <div class="brand red"><span class="dot"></span>Qarawan Silk</div>
  <div class="name">Khalid Omar Al Fayez <span class="ar">خالد عمر الفايز</span></div>
  <div class="title">Chief Executive Officer · <span class="ar">مدير التنفيذي</span></div>
  <ul class="contacts small">
    <li><i></i>+966 12 6847315 Ext. 354</li>
    <li><i></i>khalidomar.fayez@qarawansilk.com</li>
    <li><i></i>www.qarawansilk.com</li>
  </ul>
  <div class="address small">
    <b>Qarawan Silk</b><br>Rimal Plaza Business Center<br>Sawari Street, Jeddah 21587<br>Kingdom of Saudi Arabia
  </div>
</section>

<!-- business card, maroon back variant -->
<section class="piece card card-red bottom">
  <div class="brand gold"><span class="dot"></span>Qarawan Silk</div>
  <div class="badges"><span></span><span role="img" aria-label="QR code"></span><span></span></div>
</section>

<!-- DL envelope, front -->
<section class="piece envelope envelope-front">
  <div class="band"><div class="brand gold"><span class="dot"></span>Qarawan Silk</div></div>
  <div class="sender">
    <b>Qarawan Silk</b><br>Rimal Plaza Business Center<br>Sawari Street, Jeddah 21587<br>Kingdom of Saudi Arabia
  </div>
</section>

<!-- DL envelope, back with flap -->
<section class="piece envelope envelope-back">
  <svg width="480" height="230" viewBox="0 0 480 230">
    <polygon points="0,0 480,0 480,44 262,68 218,68 0,44" fill="var(--maroon)"/>
    <polyline points="0,44 218,68 262,68 480,44" fill="none" stroke="var(--gold)" stroke-width="2"/>
  </svg>
  <div class="brand gold"><span class="dot"></span>Qarawan Silk</div>
</section>

<!-- A4 letterhead -->
<section class="piece letterhead">
  <header class="band">
    <div class="brand gold"><span class="dot"></span>Qarawan Silk</div>
    <div class="col address"><b>Qarawan Silk</b><br>Rimal Plaza Business Center<br>Sawari Street, Jeddah 21587<br>Kingdom of Saudi Arabia</div>
    <div class="col contact">+966 12 6847315 Ext. 354<br>+966 12 6847316<br>khalidomar.fayez@qarawansilk.com<br>www.qarawansilk.com</div>
  </header>
  <div class="signature" role="img" aria-label="Handwritten signature"></div>
  <div class="signee">
    <div class="name">Khalid Omar Al Fayez</div>
    <div class="role">Chief Executive Officer</div>
  </div>
</section>

</body>
</html>
```